Brightfield Optics seeks updated contemporary business card

Brightfield Optics utilizes advanced technology and we take pride in the modern look and feel of our practice. We like our current card, but it's been four years so it is time for an update.

Target Market(s)

Females 25-45 make the most health care decisions for their family.

Contact Information for Business Card

Clean front. Back with info and with empty space for appointment time or other small note

Requirements
Must have
• Logo
Ridge Marketvale, 28413 E Larkspur Ave
Cedar Terrace Marketvale, 4638 S Dunmore Rd
Call or text: 509-342-1968
email: hello@brightfieldoptics.example
brightfieldoptics.example
Dr Tobias Werring & Associates

```html
<!DOCTYPE html>
<html lang="en">
<head>
<meta charset="utf-8">
<title>Brightfield Optics – Business Card</title>
<link rel="stylesheet" href="https://fonts.googleapis.com/css2?family=Bitter:wght@500;700&display=swap">
<style>
  :root {
    --navy: #1f3b73;
    --blue-deep: #2b4f8a;
    --blue-mid: #0f7fbf;
    --blue-bright: #0a9fd8;
    --blue-line: #5cc6f0;
    --paper: #ffffff;
    --stage: #e9ecef;
  }
  * { box-sizing: border-box; margin: 0; padding: 0; }
  html, body {
    width: 1200px; height: 900px; overflow: hidden;
    background: var(--stage);
    font-family: "Bitter", Georgia, serif;
  }
  .canvas {
    position: relative; width: 1200px; height: 900px;
  }
  .card {
    position: absolute; left: 285px; width: 630px; height: 360px;
    overflow: hidden; border-radius: 3px;
    box-shadow: 0 10px 28px rgba(20, 40, 70, 0.22);
  }
  .card-front {
    top: 75px;
    background: linear-gradient(160deg, var(--blue-deep) 0%, var(--blue-mid) 60%, var(--blue-bright) 100%);
    display: flex; align-items: center; justify-content: center;
  }
  .brand {
    display: flex; align-items: center; gap: 14px;
    color: var(--navy); font-weight: 700; text-transform: uppercase;
  }
  .brand-dot { border-radius: 50%; background: var(--navy); flex: none; }
  .card-front .brand { font-size: 44px; letter-spacing: 1px; }
  .card-front .brand-dot { width: 26px; height: 26px; }

  .card-back { top: 475px; background: var(--paper); }
  .wave { position: absolute; left: 0; top: 0; width: 630px; height: 360px; }
  .corner-mark {
    position: absolute; left: 20px; top: 20px; width: 22px; height: 22px;
    background: linear-gradient(135deg, var(--navy), var(--blue-bright));
  }
  .practice-name {
    position: absolute; left: 56px; top: 22px;
    font-size: 17px; font-weight: 700; color: var(--navy);
    text-transform: uppercase; letter-spacing: 0.3px;
  }
  .contact-list {
    position: absolute; left: 44px; top: 72px; list-style: none;
  }
  .contact-item {
    display: flex; align-items: center; gap: 12px; height: 28px;
    font-size: 14px; font-weight: 500; color: var(--navy);
  }
  .contact-icon {
    width: 22px; height: 22px; border: 1.5px solid var(--blue-mid);
    border-radius: 5px; display: flex; align-items: center; justify-content: center;
  }
  .contact-icon svg { width: 13px; height: 13px; fill: var(--navy); }
  .locations {
    position: absolute; left: 44px; top: 190px; list-style: none;
    font-size: 14px; font-weight: 500; color: var(--navy); line-height: 24px;
  }
  .card-back .brand {
    position: absolute; left: 370px; top: 160px; font-size: 26px;
  }
  .card-back .brand-dot { width: 18px; height: 18px; }
</style>
</head>
<body>
<main class="canvas">
  <section class="card card-front" aria-label="Card front">
    <div class="brand"><span class="brand-dot"></span>Brightfield Optics</div>
  </section>

  <section class="card card-back" aria-label="Card back">
    <svg class="wave" viewBox="0 0 630 360" aria-hidden="true">
      <defs>
        <linearGradient id="waveFill" x1="0" y1="0" x2="1" y2="1">
          <stop offset="0" stop-color="#2b4f8a"/>
          <stop offset="0.6" stop-color="#0f7fbf"/>
          <stop offset="1" stop-color="#0a9fd8"/>
        </linearGradient>
      </defs>
      <path d="M0,232 C110,330 300,300 420,312 C520,320 590,292 630,240 L630,360 L0,360 Z" fill="url(#waveFill)"/>
      <path d="M0,232 C110,330 300,300 420,312 C520,320 590,292 630,240" fill="none" stroke="#5cc6f0" stroke-width="2"/>
    </svg>
    <div class="corner-mark"></div>
    <h1 class="practice-name">Dr Tobias Werring &amp; Associates</h1>
    <ul class="contact-list">
      <li class="contact-item">
        <span class="contact-icon"><svg viewBox="0 0 24 24"><path d="M6.6 10.8a15.1 15.1 0 0 0 6.6 6.6l2.2-2.2a1 1 0 0 1 1-.25 11.4 11.4 0 0 0 3.6.57 1 1 0 0 1 1 1V20a1 1 0 0 1-1 1A17 17 0 0 1 3 4a1 1 0 0 1 1-1h3.5a1 1 0 0 1 1 1c0 1.25.2 2.45.57 3.57a1 1 0 0 1-.25 1z"/></svg></span>
        509-342-1968
      </li>
      <li class="contact-item">
        <span class="contact-icon"><svg viewBox="0 0 24 24"><path d="M2 5h20v14H2z M4 7l8 6 8-6v-0.01H4z" fill-rule="evenodd"/></svg></span>
        hello@brightfieldoptics.example
      </li>
      <li class="contact-item">
        <span class="contact-icon"><svg viewBox="0 0 24 24"><path d="M12 2a10 10 0 1 0 0 20 10 10 0 0 0 0-20zm0 2c.9 1.2 1.6 2.6 2 4h-4c.4-1.4 1.1-2.8 2-4zM4.3 14a8 8 0 0 1 0-4h3.4a16 16 0 0 0 0 4zm.8 2h3c.3 1.3.8 2.5 1.4 3.6A8 8 0 0 1 5.1 16zm3-8h-3a8 8 0 0 1 4.4-3.6C8.9 5.5 8.4 6.7 8.1 8zM12 20c-.9-1.2-1.6-2.6-2-4h4c-.4 1.4-1.1 2.8-2 4zm2.3-6H9.7a14 14 0 0 1 0-4h4.6a14 14 0 0 1 0 4zm.2 5.6c.6-1.1 1.1-2.3 1.4-3.6h3a8 8 0 0 1-4.4 3.6zm1.8-5.6a16 16 0 0 0 0-4h3.4a8 8 0 0 1 0 4zm-.4-6c-.3-1.3-.8-2.5-1.4-3.6A8 8 0 0 1 18.9 8z"/></svg></span>
        brightfieldoptics.example
      </li>
      <li class="contact-item">
        <span class="contact-icon"><svg viewBox="0 0 24 24"><path d="M12 2a7 7 0 0 0-7 7c0 5.2 7 13 7 13s7-7.8 7-13a7 7 0 0 0-7-7zm0 9.5A2.5 2.5 0 1 1 12 6.5a2.5 2.5 0 0 1 0 5z"/></svg></span>
      </li>
    </ul>
    <ul class="locations">
      <li>Ridge Marketvale, 28413 E Larkspur Ave</li>
      <li>Cedar Terrace Marketvale, 4638 S Dunmore Rd</li>
    </ul>
    <div class="brand"><span class="brand-dot"></span>Brightfield Optics</div>
  </section>
</main>
</body>
</html>
```